Pharma Business needs a new careers template

We need a new job posting template to use for all of our open positions. We are in the pharma production business and want to elevate our job postings. The design should incorporate our company colours (namely blue and white).<br/><br/>The completed work should look professional, innovative and slightly quirky.<br/><br/>Feel free to familiarise yourself with some of our current designs on our website (www.tavoro.com).<br/><br/>We have a few ideas of how we want the template to look like:<br/><br/>- We would like the design to incorporate various boxes that show different information like "Role Profile", "Benefits" etc.<br/><br/>- We would like to show some of our achievements in a special type of ellipses that remind of tablets or capsules. See a close example of another job posting incorporating similar design (but with circles instead of capsules/tablets) attached.<br/><br/>- We would like some of the main information like job location, contact phone etc to be shown after a corresponding icon. Example screenshot applied.<br/><br/>We have also attached an example job posting to give you an idea of what information our template should hold.

Industry/Entity Type

Pharmaceutical

Colors
33a6d7
ffffff
0393ce
3277b5

Requirements
Must have
• The file should be editable so we can freely fill it for each new position. We should also have it in PSD format.

```html
<!DOCTYPE html>
<html lang="en">
<head>
<meta charset="utf-8">
<title>Tavoro Pharma – Job Posting</title>
<link href="https://fonts.googleapis.com/css2?family=Montserrat:wght@400;500;700;800;900&display=swap" rel="stylesheet">
<style>
:root{
  --page-bg:#dcdcdc;
  --paper:#ffffff;
  --panel:#efefef;
  --blue-deep:#3277b5;
  --blue-bright:#0393ce;
  --blue-light:#33a6d7;
  --heading:#2f79b8;
  --ink:#2b2b2b;
  --bar:#3a3a3a;
  --brand:#3a3f6b;
}
*{margin:0;padding:0;box-sizing:border-box}
html,body{width:707px;height:1200px;overflow:hidden}
body{background:var(--page-bg);font-family:"Montserrat",Arial,sans-serif;position:relative}
.flyer-frame{position:absolute;left:20px;top:127px;width:667px;height:946px;box-shadow:0 4px 14px rgba(0,0,0,.25)}
.flyer{position:absolute;left:0;top:0;width:834px;height:1182px;background:var(--paper);transform:scale(.8);transform-origin:0 0;color:var(--ink)}
.panel{position:absolute;left:40px;top:0;width:754px;height:1000px;background:var(--panel)}
.brand{position:absolute;left:100px;top:28px;display:flex;align-items:center;gap:10px}
.brand-dot{width:18px;height:18px;border-radius:50%;background:var(--brand);flex:none}
.brand-name{font-weight:700;font-size:20px;line-height:22px;color:var(--brand)}
.job-title{position:absolute;left:0;width:834px;top:44px;text-align:center;font-weight:800;font-size:40px;line-height:48px;color:var(--blue-bright)}
.title-bar{position:absolute;left:395px;top:96px;width:42px;height:4px;background:var(--bar)}
.web-pill{position:absolute;left:612px;top:48px;width:182px;height:33px;background:var(--blue-bright);border-radius:17px 0 0 17px;color:#fff;font-size:17px;line-height:33px;text-align:center}
.web-pill b{font-weight:700}
.copy{position:absolute;left:60px;width:714px;text-align:center;font-size:13.6px;line-height:17.6px}
.intro-1{top:117px}
.intro-2{top:200px}
.band{position:absolute;left:40px;width:754px;border-radius:0 0 64px 64px}
.role-band{top:292px;height:208px;background:var(--blue-deep)}
.benefits-band{top:764px;height:225px;background:var(--blue-bright);left:42px;width:752px}
.badge{position:absolute;width:64px;height:64px;border-radius:50%;background:#fff;box-shadow:6px 6px 10px rgba(0,0,0,.22);display:flex;align-items:center;justify-content:center}
.role-badge{left:377px;top:260px}
.benefits-badge{left:367px;top:732px}
.band-title{position:absolute;left:0;width:834px;text-align:center;color:#fff;font-weight:800;font-size:28px}
.role-title{top:336px}
.benefits-title{top:804px}
.role-copy{top:385px;color:#fff}
.section-heading{position:absolute;left:0;width:834px;text-align:center;color:var(--heading);font-weight:800;font-size:29px}
.skills-heading{top:518px}
.challenge-heading{top:1010px}
.list{position:absolute;list-style:none;font-size:13.6px;line-height:17.6px}
.list li{position:absolute;left:0;white-space:nowrap;padding-left:28px}
.list svg{position:absolute;left:0;top:1px;width:16px;height:16px}
.skills-left{left:84px;top:0}
.skills-right{left:410px;top:0}
.benefits-list{color:#fff}
.benefits-left{left:86px;top:0}
.benefits-right{left:451px;top:0}
.challenge-copy{top:1057px;color:#333}
</style>
</head>
<body>
<div class="flyer-frame">
<div class="flyer">
  <div class="panel"></div>

  <div class="brand"><span class="brand-dot"></span><span class="brand-name">Tavoro<br>Pharma</span></div>
  <h1 class="job-title">JOB TITLES</h1>
  <div class="title-bar"></div>
  <div class="web-pill">www.<b>tavoro</b>.com</div>

  <p class="copy intro-1">Habitasse porta luctus porta. Aptent augue. Justo aliquet urna justo. Inceptos ligula elit aenean maecenas montes ullamcorper commodo volutpat Massa aliquam velit interdum viverra congue malesuada lacus lobortis egestas malesuada blandit nec facilisis. Fermentum tempor arcu litora fringilla, quis aenean sagittis feugiat a pretium hendrerit sociosqu mattis, maecenas.</p>
  <p class="copy intro-2">Turpis lorem. Aliquet nibh sociis mus facilisi interdum aliquet aenean sem vulputate natoque. Malesuada rutrum sociosqu sociosqu litora nunc ornare feugiat volutpat feugiat natoque dictumst scelerisque sociis ornare Eget inceptos quam interdum.</p>

  <div class="band role-band"></div>
  <div class="badge role-badge">
    <svg width="36" height="36" viewBox="0 0 36 36"><circle cx="18" cy="12" r="7" fill="#3277b5"/><path d="M4 31c1-8 7-12 14-12s13 4 14 12z" fill="#3277b5"/></svg>
  </div>
  <h2 class="band-title role-title">Role Profile:</h2>
  <p class="copy role-copy">Velit Commodo, ultrices proin tellus montes magnis mi porttitor metus sociis condimentum dis platea. Ad consectetuer laoreet euismod ad donec tellus elit ad metus lectus. Sit pretium quis imperdiet velit turpis diam urna torquent ante phasellus nascetur per euismod ultrices consectetuer a. Sollicitudin lobortis scelerisque vel senectus id, pharetra iaculis non sem id nam odio fames facilisi quam integer condimentum rutrum pulvinar inceptos. Montes id nonummy platea, mattis proin cum.</p>

  <h2 class="section-heading skills-heading">To be successful in this role you should have:</h2>
  <ul class="list skills-left">
    <li style="top:573px"><svg viewBox="0 0 16 16"><circle cx="8" cy="8" r="8" fill="#33a6d7"/><path d="M4.5 8.2l2.4 2.3 4.6-4.8" stroke="#fff" stroke-width="1.8" fill="none"/></svg>Cubilia. Porta. Morbi aliquet aptent<br>Aenean nostra purus.</li>
    <li style="top:624px"><svg viewBox="0 0 16 16"><circle cx="8" cy="8" r="8" fill="#33a6d7"/><path d="M4.5 8.2l2.4 2.3 4.6-4.8" stroke="#fff" stroke-width="1.8" fill="none"/></svg>Rhoncus vitae mus fermentum<br>placerat placerat libero.</li>
    <li style="top:676px"><svg viewBox="0 0 16 16"><circle cx="8" cy="8" r="8" fill="#33a6d7"/><path d="M4.5 8.2l2.4 2.3 4.6-4.8" stroke="#fff" stroke-width="1.8" fill="none"/></svg>Interdum, dapibus aliquet dignissim<br>hac fusce non. Consectetuer.</li>
    <li style="top:725px"><svg viewBox="0 0 16 16"><circle cx="8" cy="8" r="8" fill="#33a6d7"/><path d="M4.5 8.2l2.4 2.3 4.6-4.8" stroke="#fff" stroke-width="1.8" fill="none"/></svg>Quam hac, ornare hendrerit ultricies.</li>
  </ul>
  <ul class="list skills-right">
    <li style="top:573px"><svg viewBox="0 0 16 16"><circle cx="8" cy="8" r="8" fill="#33a6d7"/><path d="M4.5 8.2l2.4 2.3 4.6-4.8" stroke="#fff" stroke-width="1.8" fill="none"/></svg>Netus parturient elementum, nisi purus dui.</li>
    <li style="top:614px"><svg viewBox="0 0 16 16"><circle cx="8" cy="8" r="8" fill="#33a6d7"/><path d="M4.5 8.2l2.4 2.3 4.6-4.8" stroke="#fff" stroke-width="1.8" fill="none"/></svg>Justo sodales, suspendisse fermentum,<br>quisque fermentum quisque pulvinar.</li>
    <li style="top:672px"><svg viewBox="0 0 16 16"><circle cx="8" cy="8" r="8" fill="#33a6d7"/><path d="M4.5 8.2l2.4 2.3 4.6-4.8" stroke="#fff" stroke-width="1.8" fill="none"/></svg>Convallis lectus feugiat suspendisse ullamcorper<br>nonummy duis pretium.Eget pretium per tempor<br>natoque. Quisque.</li>
  </ul>

  <div class="band benefits-band"></div>
  <div class="badge benefits-badge">
    <svg width="34" height="34" viewBox="0 0 34 34"><rect x="5" y="20" width="4" height="10" fill="#33a6d7"/><rect x="12" y="15" width="4" height="15" fill="#3277b5"/><rect x="19" y="18" width="4" height="12" fill="#33a6d7"/><rect x="26" y="10" width="4" height="20" fill="#3277b5"/><path d="M4 17l8-7 7 4 10-9" stroke="#3277b5" stroke-width="2" fill="none"/><path d="M25 5h5v5" stroke="#3277b5" stroke-width="2" fill="none"/></svg>
  </div>
  <h2 class="band-title benefits-title">Benefits:</h2>
  <ul class="list benefits-list benefits-left">
    <li style="top:854px"><svg viewBox="0 0 16 16"><circle cx="8" cy="8" r="7" stroke="#fff" stroke-width="1.6" fill="none"/><path d="M4.8 8.2l2.2 2.1 4.2-4.4" stroke="#fff" stroke-width="1.6" fill="none"/></svg>Nonummy fermentum nec dictumst et.</li>
    <li style="top:890px"><svg viewBox="0 0 16 16"><circle cx="8" cy="8" r="7" stroke="#fff" stroke-width="1.6" fill="none"/><path d="M4.8 8.2l2.2 2.1 4.2-4.4" stroke="#fff" stroke-width="1.6" fill="none"/></svg>Venenatis. Aenean ac. Commodo volutpat<br>dolor libero mus.</li>
    <li style="top:942px"><svg viewBox="0 0 16 16"><circle cx="8" cy="8" r="7" stroke="#fff" stroke-width="1.6" fill="none"/><path d="M4.8 8.2l2.2 2.1 4.2-4.4" stroke="#fff" stroke-width="1.6" fill="none"/></svg>Cras consequat, non tempor justo.</li>
  </ul>
  <ul class="list benefits-list benefits-right">
    <li style="top:854px"><svg viewBox="0 0 16 16"><circle cx="8" cy="8" r="7" stroke="#fff" stroke-width="1.6" fill="none"/><path d="M4.8 8.2l2.2 2.1 4.2-4.4" stroke="#fff" stroke-width="1.6" fill="none"/></svg>Natoque potenti Hymenaeos ad tristique<br>torquent ultrices. Nec donec. Eu.</li>
    <li style="top:899px"><svg viewBox="0 0 16 16"><circle cx="8" cy="8" r="7" stroke="#fff" stroke-width="1.6" fill="none"/><path d="M4.8 8.2l2.2 2.1 4.2-4.4" stroke="#fff" stroke-width="1.6" fill="none"/></svg>Ac consequat ridiculus convallis<br>curae; porttitor.</li>
    <li style="top:944px"><svg viewBox="0 0 16 16"><circle cx="8" cy="8" r="7" stroke="#fff" stroke-width="1.6" fill="none"/><path d="M4.8 8.2l2.2 2.1 4.2-4.4" stroke="#fff" stroke-width="1.6" fill="none"/></svg>Lobortis non hendrerit taciti sed. Cursus.</li>
  </ul>

  <h2 class="section-heading challenge-heading">Challenged by this career opportunity?</h2>
  <p class="copy challenge-copy">urae; eros cubilia suspendisse netus turpis laoreet nonummy vivamus scelerisque rutrum.<br>Risus porttitor semper erat lorem ante orci cum natoque mauris lobortis. Velit semper aliquet. Metus proin ullamcorper augue urna. Eros taciti maecenas est, aliquam parturient etiam gravida nullam molestie. Sem imperdiet.Porta praesent sit. Vitae pede luctus et potenti ac augue primis cum vel. Blandit scelerisque tincidunt tincidunt luctus pretium eleifend.</p>
</div>
</div>
</body>
</html>
```